Brisk Lyceum Website

We are looking for a new design of our website. The current website is www.brisklyceum-example.com. The company is the #1 pre-college math and science program in Coral County, CA. We would like to see designs that integrate our logo with a modern color scheme. We are also open for suggestions that could improve our logo. We would like a simple, minimal, clean, classy, and vibrant front-page user interface design that give the premium, modern, innovative, creative, and premier brand feel. We like the "New Retro Colors for the Web" as described here: http://www.pixelharbor-example.net/en/layout-notes-2013/.

Target Market(s)

The target market is parents with K-12 students from a diverse population. Parents are well educated with family income > $150,000. Most of the decision makers are mothers from immigrate families: 30% Chinese, 30% Korean, 15% Indian, 24% White.

Industry/Entity Type

College

Requirements
Must have
• Must read our statement of differentiation at:
• http://brisklyceum-example.com/about-us
• Your design must be reflective of your understanding of the statements.
Nice to have
• The design should also be mobil friendly.
Should not have
• While most of our current classes are math, our company is expanding to include STEM (Science, Technology, Engineering, and Math) for gifted students. Therefore, the site should not be JUST a math education site.

```html
<!DOCTYPE html>
<html lang="en">
<head>
<meta charset="utf-8">
<title>Brisk Lyceum — For Gifted Youth</title>
<link rel="stylesheet" href="https://fonts.googleapis.com/css2?family=Questrial&family=Open+Sans:ital,wght@0,400;0,700;1,700&display=swap">
<style>
:root{
  --brand-blue:#1f8bd3;
  --brand-blue-dark:#0f6fb3;
  --panel:#f4f5f6;
  --panel-edge:#d9dcdf;
  --ink:#1b1b1b;
  --ink-soft:#333;
  --heading-blue:#1c7fc8;
  --white:#ffffff;
  --tile-orange:#f07c1c;
  --tile-navy:#163f8f;
  --tile-green:#2a9a3b;
  --tile-amber:#f39a1e;
  --stage-top:#8a8a8a;
  --stage-bottom:#3b3b3b;
  --highlight:#1f8bd3;
}
*{box-sizing:border-box;margin:0;padding:0}
html,body{width:1200px;height:2400px;overflow:hidden}
body{background:var(--brand-blue);font-family:"Open Sans",Arial,sans-serif;color:var(--ink);position:relative}
.abs{position:absolute}

/* header */
.brand{left:78px;top:14px;color:var(--white);font-family:"Questrial",sans-serif}
.brand-name{font-size:120px;line-height:.95;letter-spacing:-2px}
.brand-tag{left:470px;top:78px;font-family:"Open Sans",sans-serif;font-weight:700;font-style:italic;font-size:36px;color:var(--white)}
.login{right:30px;top:62px;color:var(--white);font-family:"Questrial",sans-serif;font-size:38px}
.search{left:878px;top:148px;width:312px;height:40px;background:var(--white);border-radius:20px;display:flex;align-items:center;justify-content:flex-end;padding-right:12px;font-family:"Questrial",sans-serif;font-size:30px;color:var(--ink)}
.search span{border-left:2px solid var(--ink);padding-left:6px;line-height:1}
.main-nav{left:0;top:252px;width:1200px;display:flex;justify-content:space-around;padding:0 20px 0 10px;font-family:"Questrial",sans-serif;font-size:34px;color:var(--white);list-style:none}

/* carousel */
.stage{left:0;top:314px;width:1200px;height:460px;background:linear-gradient(var(--stage-top),var(--stage-bottom))}
.slide{position:absolute;box-shadow:0 6px 18px rgba(0,0,0,.5)}
.slide-main{left:336px;top:42px;width:572px;height:340px;background:linear-gradient(160deg,#c9b48c,#6a5a45 45%,#2a2420)}
.slide-side{background:linear-gradient(160deg,#9aa7b8,#4b5563)}
.scrollbar{left:252px;top:418px;width:696px;height:8px;background:#cfcfcf}
.scrollbar i{position:absolute;left:262px;top:0;width:30px;height:8px;background:var(--white)}

/* panels */
.panel{background:var(--panel);border:3px solid var(--panel-edge)}
.panel-title{font-family:"Questrial",sans-serif;color:var(--heading-blue);text-align:center}
.events{left:7px;top:785px;width:250px;height:176px}
.events .panel-title{font-size:50px;margin-top:4px}
.event-row{display:flex;justify-content:space-between;padding:14px 18px 0 12px;font-size:20px}
.event-date{text-align:right;padding-right:18px;font-size:20px}
.more{font-size:17px;font-style:italic;text-align:center;margin-top:6px}
.news{left:7px;top:972px;width:250px;height:216px}
.news .panel-title{font-size:46px;line-height:1;margin-top:2px}
.news-item{font-size:15px;padding:6px 10px 0}
.news-item .date{text-align:right}
.location{left:7px;top:1200px;width:250px;height:552px}
.location .panel-title{font-size:50px;margin-top:4px}
.loc-text{font-size:13px;padding:6px 16px;line-height:1.4}
.map{left:14px;top:166px;width:216px;height:200px;background:linear-gradient(#ffffff,#e6e6e6);border:1px solid #999}
.college-name{left:14px;top:378px;width:216px;text-align:center;font-family:"Questrial",sans-serif;font-size:24px;letter-spacing:3px;color:var(--ink-soft);border-top:2px solid var(--ink-soft);padding-top:6px}
.loc-address{left:14px;top:430px;font-size:13px;line-height:1.45}

.dashboard{left:266px;top:785px;width:678px;height:823px;background:var(--white)}
.dashboard .panel-title{text-align:left;font-size:56px;padding:4px 16px 0}
.lead{padding:6px 16px 0;font-size:19px;line-height:1.3}
.lead strong{font-style:italic}
.tiles{display:flex;gap:36px;padding:26px 16px 0 22px}
.tile{width:136px;height:136px;border:5px solid;display:flex;flex-direction:column;justify-content:flex-end;overflow:hidden}
.tile-art{flex:1;background:linear-gradient(#ffffff,#dfe6ee)}
.tile-label{color:var(--white);text-align:center;font-size:18px;font-weight:700;padding:6px 0 8px}
.tile-elearning{border-color:var(--tile-orange)}.tile-elearning .tile-label{background:var(--tile-orange)}
.tile-scheduler{border-color:var(--tile-navy)}.tile-scheduler .tile-label{background:var(--tile-navy)}
.tile-newsletter{border-color:var(--tile-green)}.tile-newsletter .tile-label{background:var(--tile-green)}
.tile-registration{border-color:var(--tile-amber)}.tile-registration .tile-label{background:var(--tile-amber)}
.howto{padding:30px 16px 0;font-size:19px;line-height:1.3}
.howto p{padding-left:28px;text-indent:-28px}
.quicklinks{padding:28px 16px 0;font-size:19px;font-weight:700;font-style:italic;line-height:1.7}

.calendar{left:953px;top:785px;width:228px;height:360px}
.calendar .panel-title{font-size:44px;margin-top:2px}
.today{text-align:center;font-family:"Questrial",sans-serif;font-size:36px;margin-top:6px}
.month{text-align:center;font-family:"Questrial",sans-serif;font-size:32px;margin-top:6px}
.cal-grid{margin:4px auto 0;border-collapse:collapse;font-size:15px}
.cal-grid td,.cal-grid th{width:24px;text-align:center;font-weight:400;line-height:1.2}
.cal-grid .is-today span{background:var(--highlight);color:var(--white);border-radius:50%;padding:0 2px}
.calendar .more{font-size:16px;margin-top:8px;line-height:1.2}

.why{left:266px;top:1620px;width:934px;height:324px;background:linear-gradient(90deg,#ffffff 60%,#e8f2f8)}
.why h2{font-family:"Open Sans",sans-serif;font-weight:400;font-size:34px;padding:18px 22px 0}
.why p{padding:14px 22px 0;width:640px;font-size:17.5px;line-height:1.3}
.why-art{right:0;top:0;width:300px;height:324px;background:radial-gradient(circle at 70% 75%,#6f8fd1,#c8d6ef 55%,transparent 75%)}

.footer{left:24px;top:2148px;width:1152px;height:216px;background:var(--white)}
.footer-brand{left:60px;top:70px;display:flex;align-items:center;gap:16px;font-family:"Questrial",sans-serif;font-size:50px;color:var(--tile-navy)}
.footer-brand i{display:block;width:54px;height:54px;border-radius:50%;background:var(--tile-green)}
.footer-copy{left:544px;top:30px;font-size:26px;line-height:1.45}
</style>
</head>
<body>

<header>
  <div class="abs brand"><div class="brand-name">Brisk<br>Lyceum</div></div>
  <div class="abs brand-tag">For Gifted Youth</div>
  <div class="abs login">Login</div>
  <div class="abs search"><span>Search</span></div>
  <ul class="abs main-nav">
    <li>Home</li><li>STEM</li><li>Science Fair</li><li>FALL 2013</li><li>Results</li>
  </ul>
</header>

<section class="abs stage" aria-label="Featured highlights">
  <div class="slide slide-side" style="left:114px;top:90px;width:40px;height:250px;opacity:.7" role="img" aria-label="Campus building photo"></div>
  <div class="slide slide-side" style="left:150px;top:74px;width:90px;height:280px" role="img" aria-label="Students at an event photo"></div>
  <div class="slide slide-side" style="left:232px;top:58px;width:110px;height:310px;background:linear-gradient(160deg,#b89a80,#5a4a3e)" role="img" aria-label="Students group photo"></div>
  <div class="slide slide-main" role="img" aria-label="Student team photo at a formal reception"></div>
  <div class="slide slide-side" style="left:906px;top:58px;width:110px;height:310px;background:linear-gradient(160deg,#5f6470,#1e2230)" role="img" aria-label="Science research photo"></div>
  <div class="slide slide-side" style="left:1010px;top:76px;width:50px;height:275px;opacity:.75" role="img" aria-label="Classroom photo"></div>
  <div class="abs scrollbar"><i></i></div>
</section>

<aside class="abs panel events">
  <h2 class="panel-title">Events</h2>
  <div class="event-row"><span>MCL 8</span><span>TBD</span></div>
  <div class="event-date">2013-11-13</div>
  <p class="more">Click here to view all Events</p>
</aside>

<aside class="abs panel news">
  <h2 class="panel-title">News</h2>
  <div class="news-item">2013 College Matriculation List<div class="date">2013-06-02</div></div>
  <div class="news-item">Lena Marsh and Owen Tarrant Qualified for the 2013 U.S. Physics Team<div class="date">2013-05-20</div></div>
  <p class="more" style="margin-top:14px">Click here to view all News</p>
</aside>

<aside class="abs panel location">
  <h2 class="panel-title">Location</h2>
  <p class="loc-text">Marlowe College, Harborview<br>All weekend classes meet at Marlowe College, Harborview.</p>
  <div class="abs map" role="img" aria-label="Street map to the campus"></div>
  <div class="abs college-name">MARLOWE</div>
  <p class="abs loc-address">Marlowe College<br>1480 Marlowe Crest<br>Harborview, CA 90410-1188<br><br>Driving Directions to<br>Marlowe College</p>
</aside>

<main class="abs panel dashboard">
  <h1 class="panel-title">Dash Board</h1>
  <p class="lead"><strong>Math Olympiad and Problem Solving Training Programs</strong><br>
  Welcome to Brisk Lyceum for Gifted Youth. We provide after-school enrichment programs in math, physics, chemistry, biology, and computer science, mentor middle and high school science research projects, and offer college counseling to aspiring students in pursuing their college dreams. Please explore this website to learn more about our programs and our approach to gifted education.</p>
  <div class="tiles">
    <div class="tile tile-elearning"><div class="tile-art" role="img" aria-label="eLearning icon"></div><div class="tile-label">eLearning</div></div>
    <div class="tile tile-scheduler"><div class="tile-art" role="img" aria-label="Scheduler clock icon"></div><div class="tile-label">Scheduler</div></div>
    <div class="tile tile-newsletter"><div class="tile-art" role="img" aria-label="Newsletter icon"></div><div class="tile-label">Newsletter</div></div>
    <div class="tile tile-registration"><div class="tile-art" role="img" aria-label="Registration tick icon"></div><div class="tile-label">Registration</div></div>
  </div>
  <div class="howto">
    <p>Click on eLearning to access our Online Learning Management System for current students and families.</p>
    <p>Click on Scheduler to make an appointment online for qualifying exams, gathering information, college counseling, or science research meetings.</p>
    <p>Click on Newsletter to subscribe to our monthly newsletter - The Brisk Learner.</p>
    <p>Click on Registration to sign up for our classes.</p>
  </div>
  <div class="quicklinks">
    <div>2013 - 2014 School Year Classes and Registration</div>
    <div>2013 Summer Programs</div>
    <div>New Student Registration</div>
  </div>
</main>

<aside class="abs panel calendar">
  <h2 class="panel-title">Calender</h2>
  <div class="today">26th Aug</div>
  <div class="month">&lt; August &gt;</div>
  <table class="cal-grid">
    <tr><th>S</th><th>M</th><th>T</th><th>W</th><th>T</th><th>F</th><th>S</th></tr>
    <tr><td>28</td><td>29</td><td>30</td><td>31</td><td>1</td><td>2</td><td>3</td></tr>
    <tr><td>4</td><td>5</td><td>6</td><td>7</td><td>8</td><td>9</td><td>10</td></tr>
    <tr><td>11</td><td>12</td><td>13</td><td>14</td><td>15</td><td>16</td><td>17</td></tr>
    <tr><td>18</td><td>19</td><td>20</td><td>21</td><td>22</td><td>23</td><td>24</td></tr>
    <tr><td>25</td><td class="is-today"><span>26</span></td><td>27</td><td>28</td><td>29</td><td>30</td><td>1</td></tr>
  </table>
  <p class="more">Click here to view<br>Complete calender</p>
</aside>

<section class="abs why">
  <h2>Why Brisk Lyceum for Gifted Youth?</h2>
  <p>In 2006, Brisk Lyceum for Gifted Youth was the first academy to offer advanced math problem solving to gifted students in Coral County. With its roots in the Harborview math community and locations proximate to Coastal State University and Marlowe College, Brisk Lyceum for Gifted Youth combines California Standardized Mathematics Curriculum with math competitions and problem solving to help gifted students to discover their passion, develop their skills, and fulfill their college dreams. To learn more about our philosophy, history, statement of differentiation, and approach to gifted education, click here.</p>
  <div class="abs why-art" role="img" aria-label="Globe with colourful question marks"></div>
</section>

<footer class="abs footer">
  <div class="abs footer-brand"><i></i>Brisk Lyceum</div>
  <p class="abs footer-copy">Copyright © 2000-2013 ,<br>Brisk Lyceum for Gifted Youth.<br>2750 Scholar Way, Suite 140 Harborview CA 90410.<br>(555) 014-2390</p>
</footer>

</body>
</html>
```